BriskwayLane.com needs updated website design.

BriskwayLane.com offers individuals a quick, hassle-free way of selling their car, rv, or boat in the Sun City Center, FL area. We will come to the customer's place of choosing in order to give them an in-person offer for their car, rv, or boat. Looking for a website design that will allow users to input their vehicle details as well as their contact info in order to schedule a time and place for our staff to come make them an offer. Currently have an active site that can be referenced.

Target Market(s)

Older people who no longer need their cars.

Industry/Entity Type

Automotive

Coding

Coded - Design and coding required

Number of Pages Required

3 page

Font styles to use
Sans Serif

Colors
a1cd3a
33b8a4

Requirements
Must have
• Trustworthy theme, Emphasis on capturing contact info (contact form visible at all times). Standard privacy policy. Wordpress theme

```html
<!DOCTYPE html>
<html lang="en">
<head>
<meta charset="utf-8">
<title>BriskwayLane.com – Sell Your Car, RV or Boat</title>
<link rel="stylesheet" href="https://fonts.googleapis.com/css2?family=Catamaran:wght@600;700;800&family=Roboto:ital,wght@0,400;0,500;0,700;1,400&display=swap">
<style>
:root{
  --green:#8dc63f;
  --green-brief:#a1cd3a;
  --teal:#33b3a0;
  --teal-dark:#2ba391;
  --navy:#0f2d5c;
  --ink:#2f2f2f;
  --muted:#555b60;
  --grey-bg:#f1f1f1;
  --footer:#2f3237;
  --white:#fff;
}
*{box-sizing:border-box;margin:0;padding:0}
html,body{width:1200px;height:3094px;overflow:hidden}
body{position:relative;font-family:Roboto,Arial,sans-serif;color:var(--ink);background:var(--white)}
.abs{position:absolute}
.heading{font-family:Catamaran,Roboto,sans-serif;font-weight:700;color:var(--ink)}
.heading .accent{color:var(--navy)}

/* header */
.site-header{position:absolute;left:0;top:0;width:1200px;height:110px;background:var(--white)}
.brand{position:absolute;left:110px;top:26px}
.brand-name{font-family:Roboto,sans-serif;font-weight:700;font-size:23px;color:var(--navy);display:flex;align-items:center;gap:12px}
.brand-dot{width:22px;height:22px;border-radius:50%;background:var(--teal)}
.brand-tag{font-size:13.5px;font-weight:700;color:var(--navy);margin-top:3px}
.call{position:absolute;left:735px;top:20px;display:flex;gap:14px;align-items:center}
.call-divider{width:1px;height:34px;background:#bbb}
.call small{display:block;font-size:11px;font-weight:500;color:#222}
.call strong{display:block;font-size:23px;font-weight:700;color:var(--navy);line-height:1.1}
.btn-sell{position:absolute;left:954px;top:20px;width:132px;height:42px;border-radius:21px;background:var(--green);color:#fff;font-weight:700;font-size:15px;display:flex;align-items:center;justify-content:center}
.main-nav{position:absolute;top:82px;left:0;width:1200px;font-size:15px;font-weight:500}
.main-nav a{position:absolute;color:#111;text-decoration:none}
.main-nav a.active{color:var(--green)}
.main-nav a.active::after{content:"";position:absolute;left:-4px;right:-4px;top:25px;height:3px;background:var(--green)}

/* hero */
.hero{position:absolute;left:0;top:110px;width:1200px;height:549px;background:linear-gradient(100deg,#c9ccce 0%,#9ea3a7 35%,#dfe1e2 60%,#b7b3a4 100%)}
.hero-title{position:absolute;left:355px;top:274px;width:490px;height:144px;background:rgba(255,255,255,.78);text-align:center;padding-top:16px}
.hero-title h1{font-family:Catamaran,sans-serif;font-weight:700;font-size:36px;line-height:40px;color:var(--navy)}
.hero-title p{font-size:17px;color:#222;margin-top:8px}

/* quote form */
.quote-form{position:absolute;left:707px;top:492px;width:379px;height:495px;background:var(--teal);border-radius:4px;overflow:hidden}
.tabs{display:flex;height:98px;border-bottom:2px solid #fff}
.tab{flex:1;display:flex;flex-direction:column;align-items:center;justify-content:center;gap:8px;color:#fff;font-size:15px;font-weight:500}
.tab+.tab{border-left:2px solid #fff}
.tab.active{background:var(--green)}
.steps{position:absolute;top:128px;left:34px;display:flex;align-items:center;gap:10px;font-size:15px}
.step-num{width:27px;height:27px;border-radius:50%;background:var(--green);color:#fff;font-size:13px;display:flex;align-items:center;justify-content:center}
.step-on{color:var(--green)}
.step-line{width:60px;height:1px;background:#7fd4c6;margin:0 12px}
.step-off{color:#d6f6f0}
.field{position:absolute;width:159px}
.field label{display:block;font-size:13.5px;font-weight:500;color:#fff;margin-bottom:8px}
.select{height:34px;background:#fff;display:flex;align-items:center;justify-content:space-between;font-size:11.5px;color:#444;padding-left:9px}
.select i{width:32px;height:34px;background:#3fd0b8;display:flex;align-items:center;justify-content:center}
.btn-order{position:absolute;left:24px;top:427px;width:333px;height:48px;background:var(--green);color:#fff;font-size:17px;font-weight:700;display:flex;align-items:center;justify-content:center;border-radius:2px}

/* why */
.feature{position:absolute;display:flex;gap:20px}
.feature-icon{width:62px;height:62px;border-radius:50%;background:#eef0ef;display:flex;align-items:center;justify-content:center;flex:none}
.feature h3{font-size:19px;font-weight:500;color:#222;margin-top:6px}
.feature p{font-size:14.5px;color:#555;margin-top:7px}

/* about */
.about{position:absolute;left:0;top:1077px;width:1200px;height:488px;background:var(--grey-bg)}
.about-text p{font-size:14.5px;line-height:26px;color:#444;width:460px;margin-bottom:13px}

/* testimonial */
.testimonial{position:absolute;left:0;top:1565px;width:1200px;height:315px;background:linear-gradient(90deg,var(--teal) 0%,#2a9f8a 55%,var(--teal) 100%)}
.testimonial h2{position:absolute;left:321px;top:60px;font-family:Catamaran,sans-serif;font-weight:700;font-size:37px;color:#fff}
.quote{position:absolute;left:322px;top:130px;width:672px;font-style:italic;font-size:16.5px;line-height:26.5px;color:#fff}
.client{position:absolute;left:322px;top:228px;color:#fff}
.client b{font-size:17px;font-weight:500;display:block}
.client span{font-size:12px;display:block;margin-top:7px}

/* how */
.step-card{position:absolute;width:230px;text-align:center}
.step-icon{width:91px;height:91px;border-radius:50%;background:var(--green);margin:0 auto;display:flex;align-items:center;justify-content:center}
.step-card h3{font-size:19px;font-weight:500;color:#222;margin-top:14px;line-height:24px}
.step-card p{font-size:14.5px;line-height:21.6px;color:#555;margin-top:8px}

/* faq */
.faq-item{position:absolute;left:112px;width:488px;height:48px;border-radius:24px;background:#fff;box-shadow:0 2px 12px rgba(0,0,0,.12);display:flex;align-items:center;justify-content:space-between;padding:0 29px;font-size:16.5px;font-weight:500;color:#111}
.faq-item b{font-size:22px;color:#111;font-weight:500}
.faq-item b.open{color:var(--green)}
.faq-answer{position:absolute;left:166px;top:2535px;font-size:13.5px;color:#444}

/* footer */
.site-footer{position:absolute;left:0;top:2814px;width:1200px;height:280px;background:var(--footer);color:#fff}
.footer-nav{position:absolute;top:112px;left:0;width:1200px;display:flex;justify-content:center;gap:26px;font-size:16px}
.footer-nav span.sep{color:#ccc}
.contact-line{position:absolute;left:112px;display:flex;align-items:center;gap:18px;font-size:14.5px}
.social{position:absolute;width:42px;height:42px;border-radius:50%;border:2px solid #fff}
.copy{position:absolute;right:112px;text-align:right;font-size:14.5px;line-height:33px;top:182px}
</style>
</head>
<body>

<header class="site-header">
  <div class="brand">
    <div class="brand-name">BriskwayLane.com <span class="brand-dot"></span></div>
    <div class="brand-tag">I'll Buy You Car Boat RV Today</div>
  </div>
  <div class="call">
    <svg width="26" height="26" viewBox="0 0 24 24" fill="none" stroke="#555" stroke-width="1.4"><path d="M5 3h4l2 5-2.5 1.5a11 11 0 0 0 6 6L16 13l5 2v4a2 2 0 0 1-2 2A17 17 0 0 1 3 5a2 2 0 0 1 2-2z"/></svg>
    <span class="call-divider"></span>
    <div><small>CALL US</small><strong>555 014 2290</strong></div>
  </div>
  <div class="btn-sell">SELL NOW</div>
  <nav class="main-nav">
    <a class="active" style="left:521px">Home</a>
    <a style="left:597px">About Us</a>
    <a style="left:695px">Why Us?</a>
    <a style="left:788px">How does it work?</a>
    <a style="left:949px">FAQ</a>
    <a style="left:1012px">Contact Us</a>
  </nav>
</header>

<section class="hero" role="img" aria-label="Photo of a hand passing car keys to another hand holding a fan of cash, car in the background"></section>
<div class="hero-title">
  <h1>Get Your Free In Person Cash<br>Offer Today</h1>
  <p>“Don’t Sell Til You Give Me A Yell”</p>
</div>

<form class="quote-form">
  <div class="tabs">
    <div class="tab active">
      <svg width="44" height="34" viewBox="0 0 44 34" fill="none" stroke="#fff" stroke-width="2"><path d="M8 14l4-10h20l4 10"/><rect x="4" y="14" width="36" height="12" rx="3"/><path d="M8 26v5h6v-5M30 26v5h6v-5"/><circle cx="11" cy="20" r="2"/><circle cx="33" cy="20" r="2"/><path d="M18 20h8"/></svg>
      Cars</div>
    <div class="tab">
      <svg width="46" height="32" viewBox="0 0 46 32" fill="none" stroke="#fff" stroke-width="2"><rect x="2" y="4" width="34" height="20" rx="2"/><path d="M36 10h5l3 6v8h-8"/><circle cx="12" cy="26" r="3"/><circle cx="36" cy="26" r="3"/><path d="M7 10h8v6H7zM20 10h8v6h-8z"/></svg>
      Rvs</div>
    <div class="tab">
      <svg width="46" height="32" viewBox="0 0 46 32" fill="none" stroke="#fff" stroke-width="2"><path d="M4 20h38l-5 6H9z"/><path d="M12 20v-7h18l5 7M18 13V7h8v6"/><path d="M2 30c4-2 6-2 10 0s6 2 10 0 6-2 10 0 6 2 10 0"/></svg>
      Boats</div>
  </div>
  <div class="steps"><span class="step-num">1</span><span class="step-on">Vehicle info</span><span class="step-line"></span><span class="step-off">2&nbsp;&nbsp;&nbsp;Contact info</span></div>

  <div class="field" style="left:25px;top:177px"><label>Year</label><div class="select">Year<i><svg width="9" height="5"><path d="M0 0h9L4.5 5z" fill="#fff"/></svg></i></div></div>
  <div class="field" style="left:198px;top:177px"><label>Make</label><div class="select">Make<i><svg width="9" height="5"><path d="M0 0h9L4.5 5z" fill="#fff"/></svg></i></div></div>
  <div class="field" style="left:25px;top:255px"><label>Model</label><div class="select">Model<i><svg width="9" height="5"><path d="M0 0h9L4.5 5z" fill="#fff"/></svg></i></div></div>
  <div class="field" style="left:198px;top:255px"><label>Mileage</label><div class="select">Enter Mileage<i><svg width="9" height="5"><path d="M0 0h9L4.5 5z" fill="#fff"/></svg></i></div></div>
  <div class="field" style="left:25px;top:334px"><label>Does It Run?</label><div class="select">Select<i><svg width="9" height="5"><path d="M0 0h9L4.5 5z" fill="#fff"/></svg></i></div></div>
  <div class="field" style="left:198px;top:334px"><label>Title Available?</label><div class="select">Select<i><svg width="9" height="5"><path d="M0 0h9L4.5 5z" fill="#fff"/></svg></i></div></div>
  <div class="btn-order">ORDER TO SCHEDULE</div>
</form>

<h2 class="heading abs" style="left:112px;top:728px;font-size:37px">Why Choose <span class="accent">Us?</span></h2>

<div class="feature" style="left:112px;top:804px">
  <div class="feature-icon"><svg width="34" height="34" viewBox="0 0 34 34" fill="none" stroke="var(--green)" stroke-width="1.6"><circle cx="17" cy="19" r="11"/><path d="M14 4h6M17 4v4M17 19l4-5"/></svg></div>
  <div><h3>Fast</h3><p>I’ll Be at Your Door Today</p></div>
</div>
<div class="feature" style="left:391px;top:804px">
  <div class="feature-icon"><svg width="34" height="34" viewBox="0 0 34 34" fill="none" stroke="var(--teal)" stroke-width="1.6"><path d="M17 4v24M8 9h18M8 9l-4 9h8zM26 9l-4 9h8zM11 29h12"/></svg></div>
  <div><h3>Fair</h3><p>Get Fair Price for Your Vehicle</p></div>
</div>
<div class="feature" style="left:112px;top:907px">
  <div class="feature-icon"><svg width="34" height="34" viewBox="0 0 34 34" fill="none" stroke="var(--teal)" stroke-width="1.6"><path d="M5 20l8-8 5 4 4-3 7 7-9 9-6-5M13 12l4-4"/></svg></div>
  <div><h3>Friendly</h3><p>Trusted for Over 25 Years</p></div>
</div>
<div class="feature" style="left:391px;top:907px">
  <div class="feature-icon"><svg width="34" height="34" viewBox="0 0 34 34" fill="none" stroke="var(--green)" stroke-width="1.6"><path d="M8 6v22M14 6v22M4 12h14M4 22h14M20 10h5a7 7 0 0 1 0 14h-5"/></svg></div>
  <div><h3>Hassle Free</h3><p>I Handle All the Paperwork</p></div>
</div>

<section class="about">
  <div class="abs" style="left:113px;top:52px;width:447px;height:372px;border-radius:45% 45% 50% 50%/40% 40% 60% 60%;background:linear-gradient(135deg,#2c4f7c 0%,#3c7fa3 50%,#8ec4dc 100%)" role="img" aria-label="Heart-shaped photo of a car key handover and a handshake"></div>
  <div class="about-text abs" style="left:620px;top:116px">
    <h2 class="heading" style="font-size:38px;color:var(--navy);margin-bottom:22px">About Us</h2>
    <p>We offer the most convenient way of selling your vehicle. We will come to you at a place of your choosing, i.e. home, office, or any other public place.&nbsp; We will give you an in person cash offer on the spot.</p>
    <p>We offer the most convenient way of selling your vehicle. We will come to you at a place of your choosing, i.e. home, office, or any other public place.&nbsp; We will give you an in person cash offer on the spot.</p>
  </div>
</section>

<section class="testimonial">
  <h2>What Our Clients Have To Say</h2>
  <svg class="abs" style="left:106px;top:158px" width="30" height="44" viewBox="0 0 30 44" fill="none" stroke="#fff" stroke-width="4"><path d="M24 4L6 22l18 18"/></svg>
  <svg class="abs" style="left:1062px;top:158px" width="30" height="44" viewBox="0 0 30 44" fill="none" stroke="#fff" stroke-width="4"><path d="M6 4l18 18L6 40"/></svg>
  <div class="abs" style="left:176px;top:116px;width:112px;height:112px;transform:rotate(45deg);background:linear-gradient(135deg,#d9e6ee,#4f7fa8);border:3px solid #fff" role="img" aria-label="Diamond-framed portrait of the client"></div>
  <svg class="abs" style="left:280px;top:116px" width="34" height="22" viewBox="0 0 34 22" fill="#5fc5b4"><circle cx="8" cy="14" r="7"/><circle cx="25" cy="14" r="7"/></svg>
  <p class="quote">Lorem ipsum dolor sit amet, consectetur adipiscing elit, sed do eiusmod tempor incididunt ut labore et dolore magna aliqua. Ut enim ad minim veniam, quis nostrud exercitation ullamco laboris nisi ut aliquip ex ea commodo consequat.</p>
  <svg class="abs" style="left:594px;top:200px" width="34" height="22" viewBox="0 0 34 22" fill="#5fc5b4"><circle cx="8" cy="8" r="7"/><circle cx="25" cy="8" r="7"/></svg>
  <div class="client"><b>Dana Reyes</b><span>Company Name</span></div>
</section>

<h2 class="heading abs" style="left:0;width:1200px;text-align:center;top:1960px;font-size:41px">How does it <span class="accent">work?</span></h2>

<div class="step-card" style="left:106px;top:2055px">
  <div class="step-icon"><svg width="50" height="36" viewBox="0 0 50 36" fill="#fff"><path d="M10 14l5-10h20l5 10h4v14h-4v6h-7v-6H17v6h-7v-6H6V14z"/><rect x="16" y="7" width="18" height="7" fill="var(--green)"/><circle cx="13" cy="21" r="3" fill="var(--green)"/><circle cx="37" cy="21" r="3" fill="var(--green)"/></svg></div>
  <h3>Enter your car details</h3>
  <p>Lorem ipsum dolor sit consectetur adipiscing elit, sed do eiusmod tempor incididunt ut</p>
</div>
<div class="step-card" style="left:357px;top:2055px">
  <div class="step-icon"><svg width="44" height="46" viewBox="0 0 44 46" fill="#fff"><circle cx="22" cy="13" r="11"/><path d="M2 46a20 16 0 0 1 40 0z"/></svg></div>
  <h3>Enter your details</h3>
  <p>Lorem ipsum dolor sit consectetur adipiscing elit, sed do eiusmod tempor incididunt ut</p>
</div>
<div class="step-card" style="left:609px;top:2055px">
  <div class="step-icon"><svg width="46" height="54" viewBox="0 0 46 54" fill="none" stroke="#fff" stroke-width="2.4"><rect x="8" y="5" width="26" height="34" rx="2"/><path d="M16 3h10v5H16zM14 16h14M14 22h14M14 28h8"/><circle cx="11" cy="43" r="8" fill="var(--green)"/><circle cx="33" cy="43" r="9" fill="var(--green)"/><path d="M33 37v12M30 40h5a2 2 0 0 1 0 4h-4a2 2 0 0 0 0 4h5"/></svg></div>
  <h3>Get your free estimate</h3>
  <p>Lorem ipsum dolor sit consectetur adipiscing elit, sed do eiusmod tempor incididunt ut</p>
</div>
<div class="step-card" style="left:860px;top:2055px">
  <div class="step-icon"><svg width="50" height="50" viewBox="0 0 50 50" fill="#fff"><rect x="4" y="8" width="32" height="30" rx="2"/><rect x="10" y="3" width="4" height="9"/><rect x="26" y="3" width="4" height="9"/><g fill="var(--green)"><rect x="9" y="18" width="5" height="4"/><rect x="17" y="18" width="5" height="4"/><rect x="25" y="18" width="5" height="4"/><rect x="9" y="26" width="5" height="4"/><rect x="17" y="26" width="5" height="4"/></g><circle cx="36" cy="36" r="11" stroke="var(--green)" stroke-width="2"/><path d="M36 30v12M30 36h12" stroke="var(--green)" stroke-width="3"/></svg></div>
  <h3>Book your appointment to sell your car</h3>
  <p>Lorem ipsum dolor sit consectetur adipiscing elit, sed do eiusmod</p>
</div>

<h2 class="heading abs" style="left:112px;top:2392px;font-size:37px">Frequently Asked <span class="accent">Questions</span></h2>
<div class="faq-item" style="top:2466px">Got an old clunker?<b class="open">–</b></div>
<p class="faq-answer">I’ll But It! – Turn it into cash today!</p>
<div class="faq-item" style="top:2579px">Got a nice car you just don’t need?<b>+</b></div>
<div class="faq-item" style="top:2647px">Got a car that needs repairs?<b>+</b></div>
<div class="abs" style="left:657px;top:2377px;width:430px;height:342px;background:linear-gradient(120deg,#e9ecdc 0%,#b8bca6 50%,#6f7460 100%)" role="img" aria-label="Photo of a man in a suit holding out a fan of dollar bills"></div>

<footer class="site-footer">
  <div class="abs" style="left:0;width:1200px;top:46px;display:flex;justify-content:center;align-items:center;gap:10px">
    <div style="text-align:right">
      <div style="font-size:16px;font-weight:700">BriskwayLane.com</div>
      <div style="font-size:9.5px;font-weight:700;margin-top:2px">I'll Buy You Car Boat RV Today</div>
    </div>
    <span style="width:22px;height:22px;border-radius:50%;background:var(--teal)"></span>
  </div>
  <nav class="footer-nav">
    <span>Home</span><span class="sep">|</span><span>About Us</span><span class="sep">|</span><span>Why Us?</span><span class="sep">|</span><span>FAQ</span><span class="sep">|</span><span>How does it work?</span><span class="sep">|</span><span>Contact Us</span>
  </nav>
  <div class="contact-line" style="top:180px">
    <svg width="20" height="20" viewBox="0 0 24 24" fill="none" stroke="#aaa" stroke-width="1.5"><path d="M5 3h4l2 5-2.5 1.5a11 11 0 0 0 6 6L16 13l5 2v4a2 2 0 0 1-2 2A17 17 0 0 1 3 5a2 2 0 0 1 2-2z"/></svg>555-014-2291</div>
  <div class="contact-line" style="top:222px">
    <svg width="20" height="16" viewBox="0 0 20 16" fill="none" stroke="#aaa" stroke-width="1.5"><rect x="1" y="1" width="18" height="14" rx="1"/><path d="M1 2l9 7 9-7"/></svg>info@briskwaylane.com</div>
  <span class="social" style="left:497px;top:191px"></span>
  <span class="social" style="left:552px;top:191px"></span>
  <span class="social" style="left:606px;top:191px"></span>
  <span class="social" style="left:661px;top:191px"></span>
  <div class="copy">© Copyright 2020 Briskway Lane.<br>All Rights Reserved</div>
</footer>

</body>
</html>
```